Retail korea clothing store needs a logo desgin

Retail clothing store. Our main customer is 28-35 years women. our store is located at japan town San Francisco. our theme color are black , White and sliver color. we would like modern.

Clothing

```html
<!DOCTYPE html>
<html lang="en">
<head>
<meta charset="utf-8">
<title>nuri — business card</title>
<link href="https://fonts.googleapis.com/css2?family=Questrial&display=swap" rel="stylesheet">
<style>
  :root {
    --backdrop: #d2d3d5;
    --card: #ffffff;
    --ink: #111111;
  }
  html, body {
    margin: 0;
    padding: 0;
    overflow: hidden;
  }
  body {
    width: 1017px;
    height: 1200px;
    background: var(--backdrop);
    position: relative;
    font-family: "Questrial", sans-serif;
    color: var(--ink);
  }
  .card {
    position: absolute;
    left: 191px;
    width: 635px;
    height: 360px;
    background: var(--card);
    border-radius: 38px;
  }
  .card--front { top: 191px; }
  .card--back { top: 648px; }
  .brand-name {
    position: absolute;
    left: 0;
    right: 0;
    top: 148px;
    text-align: center;
    font-size: 46px;
    line-height: 1;
    letter-spacing: 2px;
  }
  .contact {
    position: absolute;
    left: 0;
    right: 0;
    top: 294px;
    text-align: center;
    font-size: 16px;
    line-height: 26px;
    letter-spacing: 1px;
  }
  .contact .sep { margin: 0 18px; }
  .contact p { margin: 0; }
</style>
</head>
<body>
  <section class="card card--front">
    <div class="brand-name">nuri</div>
  </section>

  <section class="card card--back">
    <div class="brand-name">nuri</div>
    <div class="contact">
      <p>415.555.0148<span class="sep">//</span>hello@nuri.com<span class="sep">//</span>www.nuri.com</p>
      <p>1720 Post St. San Francisco, CA 94115</p>
    </div>
  </section>
</body>
</html>
```